VELVET ORBITS - BOOK COVER

I have written a book called VELVET ORBIT - HOW TO CLIMB PAST EVERY LIMIT TO THE TOP RUNG. I need a front cover design for the book. The book cover needs to be intriguing for someone to pick it up and read the first couple of pages. I want people to think about ACHIEVING SUCCESS when they read this book.
PLEASE LOOK AT THE ATTACHMENT. THANKS!

Target Market(s)

males, entrepreneurs, small business owners, salespeople, corporate executives

Industry/Entity Type

Business

Logo Text

VELVET ORBITS

Logo styles of interest
Emblem Logo
Abstract Logo
Font styles to use
Serif
Sans Serif

Colors
ec1f27
000000
959595
ffffff

Requirements
Must have
• It has to have a "hurricane" feel to it with hurricane colors.
Nice to have
• I open to your ideas
Should not have
• no other colors except red, black, gray, white.

```html
<!DOCTYPE html>
<html lang="en">
<head>
<meta charset="utf-8">
<title>Velvet Orbit – Book Cover</title>
<link rel="stylesheet" href="https://fonts.googleapis.com/css2?family=Roboto+Condensed:wght@700;900&display=swap">
<style>
  :root {
    --red: #ec1f27;
    --black: #000000;
    --gray: #c0c0c0;
    --storm-light: #e6e6e6;
    --storm-gray: #959595;
    --white: #ffffff;
  }
  html, body {
    margin: 0;
    padding: 0;
    width: 855px;
    height: 1200px;
    overflow: hidden;
    background: var(--gray);
  }
  .canvas {
    position: relative;
    width: 855px;
    height: 1200px;
    background: var(--gray);
    font-family: "Roboto Condensed", "Arial Narrow", sans-serif;
  }
  .cover {
    position: absolute;
    left: 104px;
    top: 116px;
    width: 646px;
    height: 967px;
    background: var(--white);
    overflow: hidden;
  }
  .title {
    position: absolute;
    left: 0;
    width: 100%;
    margin: 0;
    text-align: center;
    font-weight: 900;
    line-height: 1;
    letter-spacing: -2px;
    transform: scaleX(0.92);
  }
  .title-top {
    top: 2px;
    font-size: 186px;
    color: var(--red);
  }
  .title-bottom {
    top: 164px;
    font-size: 166px;
    color: var(--black);
  }
  .growth-chart {
    position: absolute;
    left: 38px;
    top: 332px;
    width: 590px;
    height: 336px;
  }
  .subtitle {
    position: absolute;
    left: 0;
    top: 712px;
    width: 100%;
    margin: 0;
    text-align: center;
    font-weight: 700;
    font-size: 33px;
    line-height: 48px;
    color: var(--black);
  }
  .author-band {
    position: absolute;
    left: 0;
    bottom: 0;
    width: 100%;
    height: 140px;
    background: var(--red);
    display: flex;
    align-items: center;
    justify-content: center;
  }
  .author-name {
    margin: 0;
    font-weight: 700;
    font-size: 102px;
    line-height: 1;
    color: var(--white);
    letter-spacing: -1px;
    white-space: nowrap;
    transform: scaleX(0.9);
  }
</style>
</head>
<body>
<div class="canvas">
  <article class="cover">
    <h1 class="title title-top">VELVET</h1>
    <h1 class="title title-bottom">ORBIT</h1>

    <svg class="growth-chart" viewBox="0 0 590 336" xmlns="http://www.w3.org/2000/svg">
      <defs>
        <linearGradient id="storm-fill" x1="0" y1="0" x2="1" y2="1">
          <stop offset="0" stop-color="var(--storm-light)"/>
          <stop offset="1" stop-color="var(--storm-gray)"/>
        </linearGradient>
      </defs>
      <g class="chart-grid" stroke="#000" stroke-width="2" fill="none">
        <path d="M0 0V336M39 0V336M78 0V336M117 0V336M156 0V336M195 0V336M234 0V336M273 0V336M312 0V336M351 0V336M390 0V336M429 0V336M468 0V336M507 0V336M546 0V336M588 0V336"/>
        <path d="M0 4H590M0 41H590M0 78H590M0 115H590M0 152H590M0 189H590M0 226H590M0 263H590M0 300H590M0 334H590"/>
      </g>
      <polygon class="chart-area" fill="var(--red)"
        points="0,336 100,290 165,222 250,195 330,150 430,120 520,70 590,0 590,336"/>
      <rect class="storm-illustration" role="img" aria-label="Illustration of a swirling hurricane funnel"
        x="112" y="36" width="310" height="300" rx="24" fill="url(#storm-fill)"/>
    </svg>

    <p class="subtitle">HOW TO CLIMB PAST EVERY LIMIT<br>TO THE TOP RUNG</p>

    <footer class="author-band">
      <p class="author-name">NOAH CALDWELL</p>
    </footer>
  </article>
</div>
</body>
</html>
```